Willowmere Haven tri-fold brochure

We are a small assisted living in a home-like environment. Brochure should be warm, heartfelt and include the list of services we provide (see existing brochure). I also want the front picture replaced with stock photo (so no picture of owners). New name to use (instead of Hester) is Dorian Feltrowe, and email is feltrowe@quintmail.example. Address is same. If you can find better photos, that would be good, all the photos here are dated. We are looking for a more professional design that still conveys warmth, because we are in a home-setting and only care for 9 residents.

Target Market(s)

35-55 year old children looking for an assisted living because their parents are unable to care for them.

Industry/Entity Type

Environment

Contact Information for Business Card

Dorian Feltrowe
Willowmere Haven or Willowmere Haven Assisted Living
40718 Pinegrove Ln. Conroe, TX 77519
281-647-5192

Requirements
Must have
• List of services offered (feel free to re-word or add/change)
• Be sure to change "Hester/Hestie" to Dorian / Dorian Feltrowe

```html
<!DOCTYPE html>
<html lang="en">
<head>
<meta charset="utf-8">
<title>Willowmere Haven – Tri-fold Brochure</title>
<link href="https://fonts.googleapis.com/css2?family=Raleway:wght@400;500;600;700;800&display=swap" rel="stylesheet">
<style>
  :root{
    --gold:#a8872c;
    --charcoal:#444446;
    --ink:#2b2b2b;
    --paper:#ffffff;
    --backdrop:#e4e3e1;
    --panel-w:240px;
  }
  *{box-sizing:border-box;margin:0;padding:0}
  html,body{width:1200px;height:868px;overflow:hidden;background:var(--backdrop)}
  body{font-family:"Raleway",sans-serif;color:var(--ink)}
  .brochure{position:relative;width:1200px;height:868px;display:flex}
  .panel{position:relative;width:var(--panel-w);height:868px;background:var(--paper);overflow:hidden}
  .panel + .panel{border-left:1px solid #e6e2d8}
  .band-top{position:absolute;left:0;top:0;width:100%;height:46px}
  .band-bottom{position:absolute;left:0;bottom:0;width:100%;height:300px}
  .panel-body{position:relative;padding:60px 18px 0 20px}
  .panel-title{font-weight:700;color:var(--gold);font-size:21px;line-height:1.15;letter-spacing:.4px;margin-bottom:14px}
  .lead{font-weight:800;font-size:14px;margin-bottom:4px}
  .copy{font-size:12.5px;line-height:1.45;margin-bottom:12px}
  .photo{background:linear-gradient(160deg,#dfe3ea 0%,#b9c4d4 45%,#e8d6d2 100%)}
  .contact-name{font-weight:700;font-size:16px}
  .contact-phone{font-size:14px;letter-spacing:.5px}

  /* testimonials */
  .quote-list{list-style:none}
  .quote-list li{position:relative;padding-left:15px;font-size:12.5px;line-height:1.42;margin-bottom:13px}
  .quote-list li::before{content:"";position:absolute;left:0;top:6px;width:6px;height:6px;border-radius:50%;background:var(--gold)}
  .testimonials .photo{position:absolute;left:0;top:560px;width:100%;height:140px;background:linear-gradient(150deg,#e9e2dc 0%,#c9a9a0 55%,#b7868a 100%)}
  .office{position:absolute;left:0;right:0;bottom:22px;color:#fff;text-align:center;font-size:11.5px;line-height:1.5}
  .office .contact-name{font-size:15px}

  /* cover */
  .cover .brand{position:absolute;top:68px;left:0;right:0;text-align:center}
  .brand-name{font-weight:600;font-size:26px;line-height:1.15}
  .brand-tag{position:absolute;top:182px;left:0;width:226px;height:30px;background:var(--gold);
    border-radius:0 15px 15px 0;color:#fff;font-size:11.5px;font-weight:500;display:flex;align-items:center;padding-left:16px}
  .cover .photo{position:absolute;top:226px;left:0;width:100%;height:400px}
  .cover-text{position:absolute;bottom:0;left:0;width:100%;height:250px;color:#fff;text-align:center;padding:72px 14px 0}
  .cover-text .pledge{font-size:16px;line-height:1.28;font-weight:500}
  .rule{height:1px;background:linear-gradient(90deg,transparent,#fff,transparent);margin:16px 8px 12px}

  /* services */
  .services-list{list-style:none}
  .services-list li{position:relative;padding-left:15px;font-size:12px;line-height:1.38;margin-bottom:13px;font-weight:500}
  .services-list li::before{content:"";position:absolute;left:0;top:5px;width:6px;height:6px;border-radius:50%;background:var(--gold)}
  .services-contact{position:absolute;left:20px;bottom:130px;color:#fff}
  .services-contact .contact-name{font-size:20px;letter-spacing:.8px}
  .services-contact .contact-phone{font-size:18px;letter-spacing:1.2px}

  /* home */
  .home .copy{font-weight:500}
  .home .photo{position:absolute;left:20px;bottom:150px;width:200px;height:160px;border-radius:50%;
    border:4px solid var(--charcoal);background:linear-gradient(150deg,#f3efe9 0%,#d9c2b0 50%,#efe6dc 100%)}
</style>
</head>
<body>
<main class="brochure">

  <section class="panel testimonials">
    <svg class="band-top" viewBox="0 0 240 46" preserveAspectRatio="none" aria-hidden="true"><path d="M0 0H240V18L0 28Z" fill="var(--gold)"/></svg>
    <div class="panel-body">
      <h2 class="panel-title">Testimonials</h2>
      <ul class="quote-list">
        <li>My mom lived in two other homes before coming to Dorian Feltrowe. Now she says this is my home.</li>
        <li>“I lived alone for years and I seemed to lose my spark. Here is where I found comfort again.”</li>
        <li>“I'd be happy to recommend them. If you are looking for caring people, look no further.”</li>
        <li>“Trust your loved one to us.”</li>
        <li>Discover the warmth of full service care in a real home.</li>
      </ul>
    </div>
    <div class="photo" role="img" aria-label="Stock photo of an elderly woman relaxing in a cosy sweater"></div>
    <svg class="band-bottom" viewBox="0 0 240 300" preserveAspectRatio="none" aria-hidden="true">
      <path d="M0 120Q120 100 240 110V300H0Z" fill="var(--charcoal)"/>
      <path d="M0 134Q120 114 240 124V300H0Z" fill="#fff"/>
      <path d="M0 142Q120 122 240 132V300H0Z" fill="var(--gold)"/>
    </svg>
    <address class="office" style="font-style:normal">
      <p class="contact-name">Dorian Feltrowe</p>
      <p>40718 Pinegrove Ln.</p>
      <p>Conroe, TX 77519</p>
      <p>feltrowe@quintmail.example</p>
      <p class="contact-phone">281-647-5192</p>
    </address>
  </section>

  <section class="panel cover">
    <svg class="band-top" viewBox="0 0 240 46" preserveAspectRatio="none" aria-hidden="true"><path d="M0 0H240V22L0 30Z" fill="var(--gold)"/></svg>
    <div class="brand"><div class="brand-name">Willowmere<br>Haven</div></div>
    <div class="brand-tag">Assisted Living &amp; Memory Care</div>
    <div class="photo" role="img" aria-label="Stock photo of a caregiver in scrubs offering water to an elderly woman in bed"></div>
    <svg class="band-bottom" viewBox="0 0 240 300" preserveAspectRatio="none" aria-hidden="true">
      <path d="M0 40Q110 -10 240 60V300H0Z" fill="var(--charcoal)"/>
      <path d="M0 62Q110 14 240 82V300H0Z" fill="#fff"/>
      <path d="M0 72Q110 26 240 92V300H0Z" fill="var(--gold)"/>
    </svg>
    <div class="cover-text">
      <p class="pledge">Offering a true and noble commitment to the highest standards of care in the industry.</p>
      <div class="rule"></div>
      <p class="contact-name">Dorian Feltrowe</p>
      <p class="contact-phone">281-647-5192</p>
    </div>
  </section>

  <section class="panel why">
    <svg class="band-top" viewBox="0 0 240 46" preserveAspectRatio="none" aria-hidden="true"><path d="M0 0H240V26L0 18Z" fill="var(--gold)"/></svg>
    <div class="panel-body">
      <h2 class="panel-title">Why Willowmere Haven?</h2>
      <p class="lead">Choosing the right place</p>
      <p class="copy">for your loved one is an important decision. Willowmere Haven is here to give you peace of mind.</p>
      <p class="copy">We are a small residential home offering a wonderful alternative to traditional assisted living. Our residents are treated like family in a warm, home-like setting.</p>
      <p class="copy">We keep every resident safe, comfortable and cared for by those who truly love what they do.</p>
    </div>
    <svg class="band-bottom" viewBox="0 0 240 300" preserveAspectRatio="none" aria-hidden="true">
      <path d="M0 150Q120 130 240 120V300H0Z" fill="var(--charcoal)"/>
      <path d="M0 166Q120 146 240 136V300H0Z" fill="#fff"/>
      <path d="M0 176Q120 156 240 146V300H0Z" fill="var(--gold)"/>
    </svg>
  </section>

  <section class="panel services">
    <svg class="band-top" viewBox="0 0 240 46" preserveAspectRatio="none" aria-hidden="true"><path d="M0 0H240V28L0 22Z" fill="var(--gold)"/></svg>
    <div class="panel-body">
      <h2 class="panel-title">SERVICES</h2>
      <ul class="services-list">
        <li>Medical supervision provided by visiting physicians and nursing personnel</li>
        <li>Rehabilitation, home health and hospice services available through licensed professionals</li>
        <li>Medications and incontinence management</li>
        <li>Personal attention, caregiver involvement and heightened activities focusing on hobbies, crafts, exercise, music therapy, holiday and birthday celebrations, and plant and pet therapy.</li>
        <li>Nutritious home cooked meals and snacks with emphasis on hydration.</li>
        <li>Assistance with bathing, grooming and other personal needs including daily laundry and housekeeping.</li>
      </ul>
    </div>
    <svg class="band-bottom" viewBox="0 0 240 300" preserveAspectRatio="none" aria-hidden="true">
      <path d="M0 60Q120 50 240 40V300H0Z" fill="var(--charcoal)"/>
      <path d="M0 72Q120 64 240 56V300H0Z" fill="#fff"/>
      <path d="M0 80Q120 72 240 64V300H0Z" fill="var(--gold)"/>
    </svg>
    <div class="services-contact">
      <p class="contact-name">Dorian Feltrowe</p>
      <p class="contact-phone">281-647-5192</p>
    </div>
  </section>

  <section class="panel home">
    <svg class="band-top" viewBox="0 0 240 46" preserveAspectRatio="none" aria-hidden="true"><path d="M0 0H240V10L0 30Z" fill="var(--gold)"/></svg>
    <div class="panel-body">
      <h2 class="panel-title">WILLOWMERE HAVEN IS YOUR HOME</h2>
      <p class="copy">The comforts of home in a private luxurious setting, allows loving care with dignity</p>
      <p class="copy">Private or companion rooms, elegantly furnished or personalized to your style.</p>
      <p class="copy">A living room, family room, dining room, sunroom, and kitchen residents can call their own, so they can live the way they always have.</p>
      <p class="copy">Enjoy beautiful days on the patio and in the lovely garden area with beautiful trees, flowers, birds and pets.</p>
    </div>
    <svg class="band-bottom" viewBox="0 0 240 300" preserveAspectRatio="none" aria-hidden="true">
      <path d="M0 120Q120 70 240 40V300H0Z" fill="var(--charcoal)"/>
      <path d="M0 134Q120 86 240 58V300H0Z" fill="#fff"/>
      <path d="M0 144Q120 96 240 68V300H0Z" fill="var(--gold)"/>
    </svg>
    <div class="photo" role="img" aria-label="Stock photo of a smiling senior woman embraced by her adult daughter"></div>
  </section>

</main>
</body>
</html>
```